Logistics and freight company requires website

Hi, a logistic and freight company which is based in the United States needs an industry standard website for its activities. We are into forwarding and courier goods from within United States and Canada. We deliver a wide range of goods from shipping of electronics to document, clothings, etc. The proposed website should be comtemporary and youthful. I require brilliant colors for the website. The website should be the basic things of a site. There should a category for shipping electronics, clothings, documents and others( stuffs not listed within the three I mentioned).

```html
<!DOCTYPE html>
<html lang="en">
<head>
<meta charset="utf-8">
<title>Harbor Lane Logistics</title>
<link href="https://fonts.googleapis.com/css2?family=Open+Sans:wght@400;600;700&family=Raleway:wght@600;700;800&display=swap" rel="stylesheet">
<style>
:root{
  --blue:#0b62b5;
  --yellow:#f2b91a;
  --yellow-deep:#e9a90e;
  --ink:#333;
  --muted:#555;
  --topbar:#ececec;
  --panel:#f0f0f0;
  --dark:#474747;
  --darker:#333333;
  --white:#fff;
}
*{margin:0;padding:0;box-sizing:border-box}
html,body{width:1200px;height:2786px;overflow:hidden}
body{position:relative;background:var(--white);font-family:'Open Sans',sans-serif;color:var(--ink)}
.abs{position:absolute}

/* top bar */
.topbar{left:0;top:0;width:1200px;height:37px;background:var(--topbar);font-size:12px;color:#777}
.topbar .contact{top:11px}
.topbar .pin{top:6px;width:26px;height:26px;border-radius:4px;background:var(--yellow)}
.topbar .soc{top:14px;width:9px;height:9px;border-radius:50%;background:#8a8a8a}

/* header */
.logo{left:98px;top:106px;font-family:'Open Sans',sans-serif;font-weight:700;font-size:18px;color:var(--blue);display:flex;align-items:center;gap:10px}
.logo .mark{width:30px;height:30px;border-radius:50%;background:var(--yellow)}
.nav{top:82px;height:50px;display:flex;align-items:center;font-size:13px;color:var(--yellow)}
.nav-home{left:360px;top:82px;width:110px;height:50px;background:var(--blue);color:var(--white);font-size:13px;display:flex;align-items:center;justify-content:center;clip-path:polygon(6% 0,100% 0,100% 100%,0 100%)}
.nav-quote{left:986px;top:82px;width:115px;height:50px;background:var(--blue);color:var(--white);font-size:13px;font-weight:600;display:flex;align-items:center;justify-content:center;clip-path:polygon(9% 0,100% 0,100% 100%,0 100%)}

/* hero */
.hero{left:0;top:180px;width:1200px;height:496px;background:linear-gradient(180deg,#2c3b55 0%,#6b6a63 35%,#d9922f 68%,#f5c04a 80%,#5a4a3a 100%)}
.hero h1{left:130px;top:328px;font-size:41px;font-weight:700;color:var(--white);letter-spacing:1px}
.hero p{left:132px;top:392px;width:420px;font-size:17px;font-weight:600;color:var(--yellow);line-height:30px}
.chev{top:400px}

/* services */
.service{top:572px;width:300px;text-align:center}
.service .photo{width:212px;height:212px;border-radius:50%;margin:0 auto;border:6px solid #d7d7d7;box-shadow:0 0 0 3px #fff inset}
.service h3{margin-top:22px;font-size:15px;font-weight:700;color:var(--blue)}
.service p{margin-top:14px;font-size:12.5px;line-height:22px;color:var(--ink)}
.service .more{margin-top:12px;font-size:10px;color:var(--yellow);letter-spacing:.5px}

/* why choose us */
.why-left{left:0;top:999px;width:600px;height:489px;background:linear-gradient(90deg,#e9eaec 0%,#f7f7f7 45%,#cfd2d6 75%,#3d3d3d 100%)}
.why-right{left:600px;top:999px;width:600px;height:489px;background:linear-gradient(160deg,#f4c22a 0%,var(--yellow) 55%,#e6ad17 100%)}
.why-right h2{position:absolute;left:65px;top:30px;font-family:'Raleway',sans-serif;font-weight:800;font-size:34px;color:var(--blue)}
.reason{left:668px;width:340px}
.reason h4{font-size:15.5px;font-weight:600;color:var(--white)}
.reason p{margin-top:8px;font-size:11.5px;line-height:22px;color:#fff6d8;text-align:justify}
.badge{left:561px;width:80px;height:80px;border-radius:50%;background:var(--white);display:flex;align-items:center;justify-content:center}

/* who we are */
.who h2{left:126px;top:1544px;font-family:'Raleway',sans-serif;font-weight:700;font-size:34px;color:var(--blue)}
.acc-head{left:124px;top:1614px;width:500px;height:38px;background:var(--panel);font-size:14.5px;font-weight:600;display:flex;align-items:center;justify-content:space-between;padding:0 16px}
.acc-photo{left:124px;top:1675px;width:205px;height:173px;background:linear-gradient(135deg,#c7ccd2,#8c7b62 60%,#d3b48a)}
.acc-body{left:358px;top:1694px;width:240px}
.acc-body h4{font-size:14.5px;font-weight:600;color:var(--ink);letter-spacing:.3px}
.acc-body p{margin-top:14px;font-size:12.5px;line-height:22px;text-align:justify}
.acc-list{left:124px;top:1868px;width:500px;border:1px solid #e6e6e6}
.acc-list div{height:39px;border-bottom:1px solid #e6e6e6;display:flex;align-items:center;justify-content:space-between;padding:0 16px;font-size:14.5px;font-weight:600}
.acc-list div:last-child{border-bottom:none}

/* quote */
.quote-box{left:691px;top:1560px;width:384px;height:433px;background:var(--panel)}
.quote-head{left:691px;top:1560px;width:384px;height:66px;background:var(--blue);color:var(--white);font-family:'Raleway',sans-serif;font-weight:700;font-size:32px;text-align:center;line-height:66px}
.field{height:38px;background:var(--white);font-size:13px;color:#555;padding:0 11px;display:flex;align-items:center}
.submit{left:716px;top:1935px;width:103px;height:45px;background:var(--blue);color:var(--white);font-size:16px;font-weight:600;display:flex;align-items:center;justify-content:center;box-shadow:8px 0 0 var(--yellow);clip-path:polygon(0 0,100% 0,100% 100%,0 100%)}
.submit-tab{left:812px;top:1935px;width:14px;height:45px;background:var(--yellow);clip-path:polygon(40% 0,100% 0,60% 100%,0 100%)}

/* testimonial */
.testimonial{left:0;top:2108px;width:1200px;height:280px;background:linear-gradient(135deg,#2b2621,#4a3d30 45%,#262321)}
.avatar{left:535px;top:2046px;width:130px;height:130px;border-radius:50%;background:linear-gradient(180deg,#c9b6a4,#6f6a66);border:7px solid #8b8b8b}
.quote-text{left:300px;top:2200px;width:600px;text-align:center;font-size:12.5px;line-height:23px;color:var(--white)}
.quote-name{left:0;top:2272px;width:1200px;text-align:center;font-size:13px;color:var(--yellow);font-weight:600}
.quote-role{left:0;top:2296px;width:1200px;text-align:center;font-size:12.5px;color:var(--white)}
.dots{left:588px;top:2342px;display:flex;gap:5px}
.dots span{width:5px;height:5px;border-radius:50%;background:#8a6c2a}
.dots span.on{background:var(--yellow)}

/* partners */
.partners{left:0;top:2388px;width:1200px;height:106px;background:#eeeeee;display:flex;align-items:center;justify-content:space-around;padding:0 90px}
.partner{display:flex;align-items:center;gap:9px;font-size:25px;font-weight:600;color:#4a4a4a}
.partner i{width:24px;height:24px;border-radius:50%;background:#4a4a4a;display:block}

/* footer */
.footer{left:0;top:2494px;width:1200px;height:240px;background:var(--dark);color:#d5d5d5}
.fcol{top:2538px}
.fcol h5{font-size:16.5px;font-weight:600;color:var(--white)}
.fcol p,.fcol li{font-size:11.5px;line-height:26px;color:#cfcfcf}
.fcol ul{list-style:none;margin-top:14px}
.fcol li{display:flex;align-items:center;gap:8px}
.newsletter{left:830px;top:2605px;width:270px;height:42px;display:flex}
.newsletter .input{flex:1;border:1px solid #777;font-size:11.5px;color:#ddd;display:flex;align-items:center;padding-left:14px}
.newsletter .btn{width:98px;background:var(--blue);color:var(--white);font-size:12px;display:flex;align-items:center;justify-content:center}
.fsoc{top:2667px;width:34px;height:34px;border-radius:50%;border:1px solid #cfcfcf}
.copyright{left:0;top:2734px;width:1200px;height:52px;background:var(--darker);color:#ddd;font-size:11.5px;text-align:center;line-height:52px}
</style>
</head>
<body>

<!-- top bar -->
<div class="abs topbar">
  <span class="abs contact" style="left:110px">&#9990;&nbsp; 0044 100 200 300</span>
  <span class="abs contact" style="left:265px">&#9993;&nbsp; info@harborlane.example</span>
  <span class="abs pin" style="left:802px"></span>
  <span class="abs pin" style="left:847px"></span>
  <span class="abs soc" style="left:940px"></span>
  <span class="abs soc" style="left:975px"></span>
  <span class="abs soc" style="left:1011px"></span>
  <span class="abs soc" style="left:1050px"></span>
  <span class="abs soc" style="left:1088px"></span>
</div>

<!-- header -->
<div class="abs logo"><span class="mark"></span>Harbor Lane Logistics</div>
<div class="abs nav-home">Home</div>
<div class="abs nav" style="left:478px">Our services</div>
<div class="abs nav" style="left:600px">About us</div>
<div class="abs nav" style="left:700px">Blog</div>
<div class="abs nav" style="left:778px">News</div>
<div class="abs nav" style="left:862px">Contacts</div>
<div class="abs nav-quote">Get a quote</div>

<!-- hero -->
<div class="abs hero" role="img" aria-label="Cargo airplane on a runway at sunset"></div>
<h1 class="abs hero" style="background:none;width:auto;height:auto;left:130px;top:328px;font-size:41px;font-weight:700;color:#fff;letter-spacing:1px">WE FRIEGHT TO</h1>
<p class="abs" style="left:132px;top:390px;width:420px;font-size:17px;font-weight:600;color:var(--yellow);line-height:30px">We are into forwarding and courier goods from within United States and Canada.</p>
<svg class="abs chev" style="left:38px" width="16" height="56" viewBox="0 0 16 56"><polyline points="14,2 2,28 14,54" fill="none" stroke="#fff" stroke-width="1.5"/></svg>
<svg class="abs chev" style="left:1146px" width="16" height="56" viewBox="0 0 16 56"><polyline points="2,2 14,28 2,54" fill="none" stroke="#fff" stroke-width="1.5"/></svg>

<!-- services -->
<div class="abs service" style="left:116px">
  <div class="photo" role="img" aria-label="Close-up of an electronic circuit board" style="background:linear-gradient(135deg,#1e3654,#3c5b7a 50%,#b9b3a2)"></div>
  <h3>Shipping Electronics</h3>
  <p>Lorem Ipsum is simply dummy text of the printing and typesetting industry. Lorem Ipsum has been the industry's standard dummy text ever since the 1500s.</p>
  <div class="more">READ MORE &nbsp;&#10141;</div>
</div>
<div class="abs service" style="left:448px">
  <div class="photo" role="img" aria-label="Paper boat on folded documents" style="background:linear-gradient(135deg,#e6edf3,#8aa4bd 50%,#1f2c3c)"></div>
  <h3>Shipping &nbsp;Document</h3>
  <p>Lorem Ipsum is simply dummy text of the printing and typesetting industry. Lorem Ipsum has been the industry's standard dummy text ever since the 1500s.</p>
  <div class="more">READ MORE &nbsp;&#10141;</div>
</div>
<div class="abs service" style="left:782px">
  <div class="photo" role="img" aria-label="Folded denim clothing" style="background:linear-gradient(135deg,#6f87ad,#35507e 55%,#22375a)"></div>
  <h3>Shipping Clothing's</h3>
  <p>Lorem Ipsum is simply dummy text of the printing and typesetting industry. Lorem Ipsum has been the industry's standard dummy text ever since the 1500s.</p>
  <div class="more">READ MORE &nbsp;&#10141;</div>
</div>

<!-- why choose us -->
<div class="abs why-left" role="img" aria-label="White delivery truck"></div>
<div class="abs why-right"><h2>WHY CHOOSE US</h2></div>

<div class="abs badge" style="top:1092px">
  <svg width="40" height="40" viewBox="0 0 40 40"><circle cx="20" cy="20" r="16" fill="none" stroke="var(--yellow)" stroke-width="4"/><polyline points="12,22 18,28 29,14" fill="none" stroke="var(--yellow)" stroke-width="4"/></svg>
</div>
<div class="abs reason" style="top:1094px">
  <h4>Fast Transportations Services</h4>
  <p>Lorem Ipsum is simply dummy text of the printing and type-setting industry. Lorem Ipsum has been the industry's standard dummy text ever since the 1500s.</p>
</div>

<div class="abs badge" style="top:1220px">
  <svg width="40" height="40" viewBox="0 0 40 40"><path d="M20 3 L34 9 V20 C34 29 27 35 20 37 C13 35 6 29 6 20 V9 Z" fill="none" stroke="var(--yellow)" stroke-width="3.5"/><polyline points="13,20 18,25 27,15" fill="none" stroke="var(--yellow)" stroke-width="3.5"/></svg>
</div>
<div class="abs reason" style="top:1214px">
  <h4>Safety And Reliability</h4>
  <p>Lorem Ipsum is simply dummy text of the printing and type-setting industry. Lorem Ipsum has been the industry's standard dummy text ever since the 1500s.</p>
</div>

<div class="abs badge" style="top:1346px">
  <svg width="44" height="36" viewBox="0 0 44 36"><rect x="2" y="8" width="24" height="18" fill="var(--yellow)"/><path d="M26 13 H35 L41 20 V26 H26 Z" fill="var(--yellow)"/><circle cx="11" cy="29" r="4.5" fill="#fff" stroke="var(--yellow)" stroke-width="3"/><circle cx="33" cy="29" r="4.5" fill="#fff" stroke="var(--yellow)" stroke-width="3"/></svg>
</div>
<div class="abs reason" style="top:1342px">
  <h4>Shipping World wide</h4>
  <p>Lorem Ipsum is simply dummy text of the printing and type-setting industry. Lorem Ipsum has been the industry's standard dummy text ever since the 1500s.</p>
</div>

<!-- who we are -->
<section class="who">
  <h2 class="abs">WHO WE ARE</h2>
  <div class="abs acc-head"><span>About us</span><span>&minus;</span></div>
  <div class="abs acc-photo" role="img" aria-label="Courier carrying a cardboard box"></div>
  <div class="abs acc-body">
    <h4>LOGISTIC SERVICES</h4>
    <p>Lorem Ipsum is simply dummy text of the printing and typesetting industry. Lorem Ipsum has been the industry's standard dummy text ever since the 1500s.</p>
  </div>
  <div class="abs acc-list">
    <div><span>United States</span><span>+</span></div>
    <div><span>Canada</span><span>+</span></div>
    <div><span>Canada</span><span>+</span></div>
  </div>
</section>

<!-- quote form -->
<div class="abs quote-box"></div>
<div class="abs quote-head">GET A QUOTE</div>
<svg class="abs" style="left:712px;top:1618px" width="10" height="14" viewBox="0 0 10 14"><line x1="5" y1="0" x2="5" y2="10" stroke="#9aa" stroke-width="1.5"/><circle cx="5" cy="10" r="3" fill="#9aa"/></svg>
<svg class="abs" style="left:1045px;top:1618px" width="10" height="14" viewBox="0 0 10 14"><line x1="5" y1="0" x2="5" y2="10" stroke="#9aa" stroke-width="1.5"/><circle cx="5" cy="10" r="3" fill="#9aa"/></svg>
<div class="abs field" style="left:716px;top:1643px;width:329px">Name</div>
<div class="abs field" style="left:716px;top:1695px;width:152px">Phone</div>
<div class="abs field" style="left:891px;top:1695px;width:154px">Email</div>
<div class="abs field" style="left:716px;top:1747px;width:329px">Cargo type</div>
<div class="abs field" style="left:716px;top:1798px;width:329px">Destinations</div>
<div class="abs field" style="left:716px;top:1850px;width:329px;height:72px;align-items:flex-start;padding-top:10px">Message</div>
<div class="abs submit-tab"></div>
<div class="abs submit" style="box-shadow:none">Submit</div>

<!-- testimonial -->
<div class="abs testimonial" role="img" aria-label="Stacked cardboard boxes in a warehouse"></div>
<div class="abs avatar" role="img" aria-label="Portrait of the managing director"></div>
<p class="abs quote-text">Lorem Ipsum is simply dummy text of the printing and typesetting industry. Lorem Ipsum has been the industry's standard dummy text ever since the 1500s, when an unknown printer took a galley of type and scrambled it to make a type specimen book.</p>
<div class="abs quote-name">Bonorum et Malorum</div>
<div class="abs quote-role">Managing Director</div>
<div class="abs dots"><span></span><span class="on"></span><span></span></div>

<!-- partners -->
<div class="abs partners">
  <div class="partner"><i></i>Presswork</div>
  <div class="partner"><i></i>Joinly</div>
  <div class="partner"><i></i>Magnet</div>
  <div class="partner"><i></i>Dropline</div>
  <div class="partner"><i></i>Qwery</div>
</div>

<!-- footer -->
<div class="abs footer"></div>
<div class="abs fcol" style="left:110px">
  <h5>Quick Links</h5>
  <ul>
    <li><svg width="10" height="10" viewBox="0 0 10 10"><polyline points="1,5 4,8 9,2" fill="none" stroke="#cfcfcf" stroke-width="2"/></svg>Privacy</li>
    <li><svg width="10" height="10" viewBox="0 0 10 10"><polyline points="1,5 4,8 9,2" fill="none" stroke="#cfcfcf" stroke-width="2"/></svg>Terms</li>
    <li><svg width="10" height="10" viewBox="0 0 10 10"><polyline points="1,5 4,8 9,2" fill="none" stroke="#cfcfcf" stroke-width="2"/></svg>Contact</li>
  </ul>
</div>
<div class="abs fcol" style="left:280px;width:240px">
  <h5>About Us</h5>
  <p style="margin-top:14px;text-align:justify">Lorem Ipsum is simply dummy text of the printing and typesetting industry. Lorem Ipsum has been the industry's standard dummy text ever since the 1500s.</p>
</div>
<div class="abs fcol" style="left:563px;width:240px">
  <h5>Get in Touch</h5>
  <p style="margin-top:14px">Address : 12 Runway Rd, Fieldport, WA 6100.</p>
  <p style="margin-top:16px">Phone : 08 5550 1200, 08 5550 1288</p>
  <p style="margin-top:16px">Email : info@harborlane-freight.example</p>
</div>
<div class="abs fcol" style="left:830px;width:290px">
  <h5>Sign up to News letter</h5>
  <p style="margin-top:6px;font-size:12px;color:#eee">Excepteur sint occaecat cupidatat non proident.</p>
</div>
<div class="abs newsletter"><div class="input">Enter Email</div><div class="btn">SUBSCRIBE</div></div>
<div class="abs fsoc" style="left:835px"></div>
<div class="abs fsoc" style="left:885px"></div>
<div class="abs fsoc" style="left:936px"></div>
<div class="abs copyright">Copyright @ 2016. HarborLane. All Rights Reserved.</div>

</body>
</html>
```